Flyer Design Project

opening a preschool and need to hand out flyers to advertise at an expo on Feb.1st. It is geared toward 3-4 year old potty trained children. I have more that 10+ years teaching experience and it will be a private preschool with small class sizes and individual instruction and attention. You can look at the website, it is www.brightmaplekids.net. I tried to make a flyer but I can't make it with high enough resolution. I attached the logo and my attempted flyer.

Industry/Entity Type

Preschool

```html
<!DOCTYPE html>
<html lang="en">
<head>
<meta charset="utf-8">
<title>Bright Maple Learning Center – Preschool Flyer</title>
<link rel="stylesheet" href="https://fonts.googleapis.com/css2?family=Questrial&family=Nunito+Sans:wght@700;800&family=Bitter:ital,wght@1,800&family=Crimson+Text:ital,wght@0,400;1,700&display=swap">
<style>
  :root {
    --sky: #dff1fb;
    --sky-deep: #cde9f8;
    --top-band: #00a6e3;
    --grass: #8cc63f;
    --pink: #ec0d8c;
    --sun-yellow: #f7ee2a;
    --heading-green: #1f9a48;
    --ink: #2b2b2b;
    --rule: #5f6062;
    --pill-green: #8cc63f;
    --lime: #d7e52a;
    --white: #ffffff;
  }
  * { box-sizing: border-box; margin: 0; padding: 0; }
  html, body { width: 1200px; height: 780px; overflow: hidden; }
  body {
    font-family: "Questrial", "Century Gothic", sans-serif;
    color: var(--ink);
  }
  .flyer {
    position: relative;
    width: 1200px;
    height: 780px;
    overflow: hidden;
    background: radial-gradient(ellipse at 30% 40%, #eef8fd 0%, var(--sky) 55%, var(--sky-deep) 100%);
  }
  .top-band { position: absolute; left: 0; top: 0; width: 100%; height: 21px; background: var(--top-band); }
  .grass-band { position: absolute; left: 0; bottom: 0; width: 100%; height: 33px; background: var(--grass); }

  .section-title {
    position: absolute;
    display: flex; align-items: center; gap: 10px;
    font-family: "Nunito Sans", sans-serif;
    font-weight: 800;
    font-size: 27px;
    color: var(--ink);
  }
  .who-title { left: 37px; top: 64px; color: var(--heading-green); }
  .who-title .marker { width: 17px; height: 25px; background: var(--heading-green); }
  .who-title span.label { text-decoration: underline; text-decoration-thickness: 2px; text-underline-offset: 5px; }

  .who-text {
    position: absolute; left: 45px; top: 106px; width: 460px;
    font-size: 20.5px; line-height: 27px;
  }

  .promise-band { position: absolute; left: 0; top: 170px; width: 620px; height: 230px; }
  .promise-text {
    position: absolute; left: 92px; top: 220px; width: 480px;
    color: var(--white); font-size: 23px; line-height: 30px; letter-spacing: 0.3px;
    transform: rotate(-9.5deg); transform-origin: left top;
    top: 280px;
  }

  .sun-art {
    position: absolute; left: 385px; top: 295px; width: 235px; height: 215px;
    background: radial-gradient(circle, var(--sun-yellow) 0%, rgba(247,238,42,0.55) 32%, rgba(247,238,42,0) 70%);
  }
  .stroller-art {
    position: absolute; left: 40px; top: 435px; width: 280px; height: 310px;
    background: radial-gradient(ellipse at 35% 75%, rgba(236,13,140,0.55) 0%, rgba(236,13,140,0.2) 40%, rgba(236,13,140,0) 72%);
  }

  .tagline {
    position: absolute; left: 218px; top: 570px; width: 380px;
    font-family: "Bitter", serif; font-style: italic; font-weight: 800;
    font-size: 37px; line-height: 36px; letter-spacing: -0.5px;
    color: var(--sun-yellow);
    -webkit-text-stroke: 1.2px #4a3a00;
    text-shadow: 2px 2px 0 #3a2d00;
  }

  .icon-chevron { width: 29px; height: 29px; flex: none; }
  .offer-title { left: 620px; top: 62px; }
  .offer-list { position: absolute; left: 647px; top: 107px; list-style: none; font-size: 21px; }
  .offer-list li { height: 34px; line-height: 34px; }
  .offer-list li:nth-child(3) { margin-top: 2px; }

  .schedule-pill {
    position: absolute; left: 646px; top: 249px; width: 320px; height: 29px;
    display: flex; align-items: center; gap: 8px; padding-left: 5px;
    background: var(--pill-green); border-radius: 15px;
    box-shadow: 0 0 0 2px rgba(255,255,255,0.7);
    font-family: "Crimson Text", serif; font-size: 14.5px; color: var(--white);
  }
  .schedule-pill svg { width: 21px; height: 21px; }

  .divider { position: absolute; left: 620px; width: 545px; height: 4px; }
  .divider-offer { top: 303px; }
  .divider-staff { top: 626px; }

  .staff-photo-frame { position: absolute; left: 646px; top: 348px; width: 137px; height: 147px; }
  .staff-photo-frame .frame-back { position: absolute; left: 6px; top: 6px; width: 131px; height: 141px; background: var(--pink); border-radius: 0 0 14px 0; }
  .staff-photo {
    position: absolute; left: 0; top: 0; width: 128px; height: 136px;
    background: linear-gradient(160deg, #d9d9d9 0%, #8e8e8e 55%, #3c3c3c 100%);
    border-radius: 12px 0 0 0;
  }
  .staff-title { left: 800px; top: 344px; }
  .staff-intro { position: absolute; left: 800px; top: 391px; width: 360px; font-size: 20.5px; line-height: 28px; }
  .staff-detail { position: absolute; left: 657px; top: 502px; width: 520px; font-size: 20.5px; line-height: 28.5px; }

  .forms-band { position: absolute; left: 632px; top: 665px; width: 546px; height: 40px; }
  .forms-text { position: absolute; left: 659px; top: 672px; font-size: 20.5px; color: var(--ink); }
  .fee-note {
    position: absolute; left: 620px; top: 719px; width: 545px; text-align: center;
    font-family: "Crimson Text", serif; font-style: italic; font-weight: 700; font-size: 15.5px; color: #222;
  }
</style>
</head>
<body>
<main class="flyer">
  <div class="top-band"></div>

  <section class="who-we-are">
    <h2 class="section-title who-title"><span class="marker"></span><span class="label">Who we are</span></h2>
    <p class="who-text">Bright Maple Learning Center is a private preschool geared towards potty-trained children aged 3 - 4 years old.</p>
  </section>

  <svg class="promise-band" viewBox="0 0 620 230" aria-hidden="true">
    <polygon points="0,95 90,82 90,218 0,218" fill="#f7ee2a"/>
    <polygon points="0,95 88,82 96,212 0,228" fill="#f7ee2a"/>
    <path d="M55,88 L592,5 L612,114 L70,205 Q40,150 55,88 Z" fill="#ec0d8c"/>
  </svg>
  <p class="promise-text">With a specialised curriculum, you can be assured that your child will be prepared when entering the world of education!</p>

  <div class="sun-art" role="img" aria-label="Smiling cartoon sun with rays"></div>
  <div class="stroller-art" role="img" aria-label="Pink toy stroller carrying two stick-figure children, holding balloons and a kite"></div>

  <p class="tagline">Students will love learning at Bright Maple Learning Center!</p>

  <section class="offer">
    <h2 class="section-title offer-title">
      <svg class="icon-chevron" viewBox="0 0 30 30" aria-hidden="true"><circle cx="15" cy="15" r="12.5" fill="#fff" stroke="#ec0d8c" stroke-width="3"/><path d="M12 8 L19 15 L12 22" fill="none" stroke="#ec0d8c" stroke-width="3.5" stroke-linecap="round" stroke-linejoin="round"/></svg>
      what we offer
    </h2>
    <ul class="offer-list">
      <li>Monday - Friday Classes</li>
      <li>A safe, happy fun-filled Environment</li>
      <li>Small classes allowing individual attention</li>
      <li>Lots of Creativity, Discover and Learning through Playing</li>
    </ul>
    <p class="schedule-pill">
      <svg viewBox="0 0 22 22" aria-hidden="true"><circle cx="11" cy="11" r="9.5" fill="none" stroke="#fff" stroke-width="2"/><path d="M9 6.5 L13.5 11 L9 15.5" fill="none" stroke="#fff" stroke-width="2.5" stroke-linecap="round" stroke-linejoin="round"/></svg>
      Please Call for more information on Shedules
    </p>
  </section>

  <svg class="divider divider-offer" viewBox="0 0 545 4" preserveAspectRatio="none" aria-hidden="true"><polygon points="0,2 40,0 505,0 545,2 505,4 40,4" fill="#5f6062"/></svg>

  <section class="staff">
    <div class="staff-photo-frame">
      <div class="frame-back"></div>
      <div class="staff-photo" role="img" aria-label="Portrait photo of the lead teacher"></div>
    </div>
    <h2 class="section-title staff-title">
      <svg class="icon-chevron" viewBox="0 0 30 30" aria-hidden="true"><circle cx="15" cy="15" r="12.5" fill="#fff" stroke="#ec0d8c" stroke-width="3"/><path d="M12 8 L19 15 L12 22" fill="none" stroke="#ec0d8c" stroke-width="3.5" stroke-linecap="round" stroke-linejoin="round"/></svg>
      Our Staff
    </h2>
    <p class="staff-intro">Mrs. Whitford is a Licenced teacher with 10+ years of elementary school experience.</p>
    <p class="staff-detail">She knows what your child needs to be prepared for the rigor of K-12 education, and how to build that foundation for the future.</p>
  </section>

  <svg class="divider divider-staff" viewBox="0 0 545 4" preserveAspectRatio="none" aria-hidden="true"><polygon points="0,2 40,0 505,0 545,2 505,4 40,4" fill="#5f6062"/></svg>

  <svg class="forms-band" viewBox="0 0 546 40" aria-hidden="true">
    <polygon points="14,2 546,2 532,40 0,40" fill="#8a9a1a" opacity="0.45" transform="translate(3,3)"/>
    <polygon points="14,0 543,0 529,37 0,37" fill="#d7e52a"/>
  </svg>
  <p class="forms-text">All forms can be downloaded from our website.</p>
  <p class="fee-note">you must be accepted and enrolled for application fee to be waived.</p>

  <div class="grass-band"></div>
</main>
</body>
</html>
```